VANTO Redesign

Make a more modern looking Homepage. Our page: www.vanto.at
Should look like:
www.kerno.com/at/de/
https://web.pallvik.com
https://id.montcalvet.com

Target Market(s)

furniture industry

Number of Pages Required

1 page

Font styles to use
Sans Serif

Colors
3176b5

```html
<!DOCTYPE html>
<html lang="en">
<head>
<meta charset="utf-8">
<title>VANTO – Decorative Furniture Fittings</title>
<link href="https://fonts.googleapis.com/css2?family=Lato:wght@400;700;900&display=swap" rel="stylesheet">
<style>
:root{
  --blue:#3176b5;
  --blue-dark:#1d4f98;
  --blue-link:#2a64a8;
  --ink:#222;
  --text:#555;
  --muted:#888;
  --grey:#ececec;
  --footer:#efefef;
  --white:#fff;
}
*{box-sizing:border-box;margin:0;padding:0}
html,body{width:1200px;height:3261px;overflow:hidden}
body{position:relative;font-family:"Lato",sans-serif;color:var(--ink);background:var(--white)}

/* hero */
.hero{position:absolute;left:0;top:0;width:1200px;height:695px;overflow:hidden}
.hero-photo{position:absolute;inset:0;background:
  radial-gradient(ellipse at 75% 60%,#b9b1a3 0,#6f6557 30%,transparent 60%),
  radial-gradient(ellipse at 20% 70%,#9a9488 0,#4d463c 35%,transparent 65%),
  linear-gradient(180deg,#2b2620 0%,#4a4036 45%,#3a3129 100%)}
.hero-shade{position:absolute;inset:0;background:rgba(0,0,0,.32)}
.brand{position:absolute;display:flex;align-items:center;gap:12px}
.brand-dot{width:48px;height:48px;border-radius:50%;background:var(--white)}
.brand-name{font-weight:400;font-size:40px;letter-spacing:5px;color:var(--white);line-height:1}
.nav{position:absolute;left:409px;top:64px;font-weight:900;font-size:15px;color:var(--white)}
.nav span{position:absolute;white-space:nowrap}
.top-btn{position:absolute;top:13px;height:33px;border:2px solid var(--white);color:var(--white);font-weight:700;font-size:13px;display:flex;align-items:center;justify-content:center;gap:6px}
.hero-title{position:absolute;left:0;width:1208px;top:258px;text-align:center;color:var(--white);font-weight:700;font-size:57px;line-height:64px}
.hero-sub{position:absolute;left:0;width:1208px;top:398px;text-align:center;color:var(--white);font-weight:900;font-size:23px;line-height:29px}
.dots{position:absolute;top:646px;left:562px;display:flex;gap:6px}
.dots i{width:15px;height:15px;border-radius:50%;border:2px solid var(--white);display:block}
.dots i.on{background:var(--white)}

/* features */
.feature{position:absolute;top:780px;width:310px}
.feature-icon{position:absolute;left:0;top:0;width:104px;height:104px;border-radius:50%;background:var(--blue);border:4px solid #dbe6f3}
.feature-icon svg{position:absolute;left:26px;top:26px}
.feature-title{position:absolute;left:108px;top:18px;font-size:24px;font-weight:400;white-space:nowrap}
.feature-text{position:absolute;left:108px;top:56px;width:200px;font-size:13px;line-height:18px;color:var(--muted)}
.feature-link{position:absolute;left:108px;top:128px;font-size:15px;font-weight:700;color:var(--blue-link)}

/* speciality */
.spec-band{position:absolute;left:0;top:1011px;width:1200px;height:424px;background:var(--grey)}
.badge{position:absolute;left:566px;top:980px;width:64px;height:64px;border-radius:50%;background:var(--white);display:flex;align-items:center;justify-content:center}
.badge i{width:34px;height:34px;border-radius:50%;background:#555;display:block}
.section-title{position:absolute;font-weight:700;font-size:34px;color:#333}
.spec-intro{position:absolute;left:0;width:1200px;top:1122px;text-align:center;font-size:18px;line-height:25px;color:#666}
.card{position:absolute;background:var(--white);border:2px solid #d8d8d8}
.card-photo{position:absolute;left:0;top:0;width:100%}
.spec-card{top:1233px;width:307px;height:350px}
.spec-card .card-photo{height:185px}
.spec-card h3{position:absolute;left:0;width:100%;top:205px;text-align:center;font-size:22px;line-height:26px;font-weight:700;color:#222}
.spec-card p{position:absolute;left:28px;right:28px;text-align:center;font-size:13px;line-height:18px;color:var(--muted)}
.btn{position:absolute;background:var(--blue);color:var(--white);font-weight:700;display:flex;align-items:center;justify-content:center}
.spec-btn{width:148px;height:42px;font-size:16px;top:1561px}

/* about */
.about{position:absolute;left:0;top:1735px;width:1200px;height:461px;background:linear-gradient(90deg,#3a80c2 0%,#3176b5 45%,var(--blue-dark) 100%)}
.about-circle{position:absolute;left:62px;top:1691px;width:550px;height:548px;border-radius:50%;background:var(--blue)}
.about-photo{position:absolute;left:120px;top:1775px;width:440px;height:385px;border-radius:48%;background:linear-gradient(180deg,#e6e3dc 0%,#c9c2b6 45%,#b48c62 100%)}
.about-title{position:absolute;left:600px;width:475px;top:1825px;text-align:center;color:var(--white);font-size:35px;font-weight:700}
.about-text{position:absolute;left:580px;width:500px;text-align:center;color:var(--white);font-size:18px;line-height:25px}
.about-btn{position:absolute;left:748px;top:2052px;width:170px;height:52px;border:2px solid var(--white);color:var(--white);font-weight:700;font-size:18px;display:flex;align-items:center;justify-content:center}

/* news */
.news-card{top:2359px;width:298px;height:402px;border:none;box-shadow:0 2px 10px rgba(0,0,0,.12)}
.news-card .card-photo{height:174px}
.news-card h4{position:absolute;left:26px;right:16px;top:202px;font-size:17px;line-height:21px;font-weight:700;color:var(--blue-link)}
.news-card p{position:absolute;left:26px;right:16px;top:258px;font-size:13px;line-height:18px;color:var(--muted)}
.news-btn{width:120px;height:33px;font-size:14px;top:2698px}

/* footer */
.footer{position:absolute;left:0;top:2843px;width:1200px;height:418px;background:var(--footer)}
.foot-brand .brand-dot{width:44px;height:44px;background:#222}
.foot-brand .brand-name{color:#222;font-size:36px;letter-spacing:4px}
.foot-head{position:absolute;top:2925px;font-size:17px;font-weight:900;color:#222}
.foot-list{position:absolute;font-size:16px;line-height:29px;color:#444;list-style:none}
.contact-row{position:absolute;left:380px;display:flex;align-items:flex-start;gap:14px;font-size:16px;line-height:20px;color:#444}
.social{position:absolute;left:911px;display:flex;align-items:center;gap:14px;font-size:16px;color:#444}
.social i{width:27px;height:27px;border-radius:50%;background:var(--blue);display:block}
.foot-rule{position:absolute;left:0;top:3191px;width:1200px;height:1px;background:#d5d5d5}
.copy{position:absolute;left:0;width:1200px;top:3214px;text-align:center;font-size:15px;color:#999}
</style>
</head>
<body>

<header class="hero">
  <div class="hero-photo" role="img" aria-label="Modern bathroom with wooden vanity, white basin, bathtub and towel rail"></div>
  <div class="hero-shade"></div>
  <div class="brand" style="left:124px;top:32px"><span class="brand-dot"></span><span class="brand-name">VANTO</span></div>
  <div class="top-btn" style="left:870px;width:93px">ENGLISH
    <svg width="10" height="7" viewBox="0 0 10 7"><path d="M1 1l4 4 4-4" fill="none" stroke="#fff" stroke-width="2"/></svg></div>
  <div class="top-btn" style="left:976px;width:94px">LOG IN</div>
  <nav class="nav">
    <span style="left:0">ABOUT</span>
    <span style="left:76px">BRAND NEW</span>
    <span style="left:193px">CATALOG CONFIGURATOR</span>
    <span style="left:413px">LIGHT CONFIGURATOR</span>
    <span style="left:617px">LAMP</span>
  </nav>
  <h1 class="hero-title">DECORATIVE<br>FURNITURE FITTINGS</h1>
  <p class="hero-sub">FUNCTIONALITY MEETS DESIGN.<br>BE INSPIRED BY THE VANTO COLLECTION.</p>
  <div class="dots"><i></i><i class="on"></i><i class="on"></i><i class="on"></i></div>
</header>

<section>
  <div class="feature" style="left:120px">
    <div class="feature-icon"><svg width="44" height="44" viewBox="0 0 44 44" fill="none" stroke="#fff" stroke-width="2.4"><rect x="4" y="4" width="36" height="36"/><path d="M10 34L34 10M10 24l10 10M26 8l10 10"/></svg></div>
    <div class="feature-title">BEST DESIGNS</div>
    <p class="feature-text">Morbi diam mauris viverra in gravida eu mattis in ante Morbi eget arcu Morbi porta</p>
    <div class="feature-link">Click here ›</div>
  </div>
  <div class="feature" style="left:445px">
    <div class="feature-icon"><svg width="44" height="44" viewBox="0 0 44 44" fill="none" stroke="#fff" stroke-width="2.4"><rect x="8" y="14" width="28" height="24"/><path d="M8 26h28M19 20h6M19 32h6M18 14V6h8v8M12 38v4M32 38v4"/></svg></div>
    <div class="feature-title">TOP QUALITY</div>
    <p class="feature-text">Morbi diam mauris viverra in gravida eu mattis in ante Morbi eget arcu Morbi porta</p>
    <div class="feature-link">Click here ›</div>
  </div>
  <div class="feature" style="left:778px">
    <div class="feature-icon"><svg width="44" height="44" viewBox="0 0 44 44" fill="none" stroke="#fff" stroke-width="2.4"><path d="M22 3l17 10v18L22 41 5 31V13z"/><rect x="14" y="14" width="16" height="18"/><path d="M14 20h16M22 20v12"/></svg></div>
    <div class="feature-title">TOP FURNITURE</div>
    <p class="feature-text">Morbi diam mauris viverra in gravida eu mattis in ante Morbi eget arcu Morbi porta</p>
    <div class="feature-link">Click here ›</div>
  </div>
</section>

<section>
  <div class="spec-band"></div>
  <div class="badge"><i></i></div>
  <h2 class="section-title" style="left:0;width:1200px;top:1066px;text-align:center">SPECIALITY SERVICES</h2>
  <p class="spec-intro">Allamcorper est eget tempor cursus neque mi consectetuer mi a ultricies massa est sed nisl<br>Class aptent taciti sociosqu ad litora torquent per conubia nostra</p>

  <article class="card spec-card" style="left:117px">
    <div class="card-photo" role="img" aria-label="Kitchen with wooden cabinets, gas hob and built-in oven" style="background:linear-gradient(135deg,#e7e2dc 0%,#a37a5a 55%,#5e3b26 100%)"></div>
    <h3>CATALOG<br>CONFIGURATOR</h3>
    <p style="top:264px">Morbi diam mauris viverra in gravida eu mattis in ante Morbi eget arcu</p>
  </article>
  <div class="btn spec-btn" style="left:205px">READ MORE</div>

  <article class="card spec-card" style="left:441px">
    <div class="card-photo" role="img" aria-label="Dining room with wooden table and brass pendant lamps" style="background:linear-gradient(160deg,#2d2a27 0%,#6b5a45 50%,#8a6240 100%)"></div>
    <h3>LIGHT<br>CONFIGURATOR</h3>
    <p style="top:264px">Morbi diam mauris viverra in gravida eu mattis in ante Morbi eget arcu</p>
  </article>
  <div class="btn spec-btn" style="left:530px;top:1568px">READ MORE</div>

  <article class="card spec-card" style="left:772px">
    <div class="card-photo" role="img" aria-label="Filament light bulb lamp in a dim interior" style="background:radial-gradient(circle at 35% 35%,#c89b55 0,#5a5247 35%,#3f4248 100%)"></div>
    <h3>LAMP</h3>
    <p style="top:240px">Morbi diam mauris viverra in gravida eu mattis in ante Morbi eget arcu Morbi porta libero ullamcorper</p>
  </article>
  <div class="btn spec-btn" style="left:858px">READ MORE</div>
</section>

<section>
  <div class="about"></div>
  <div class="about-circle"></div>
  <div class="about-photo" role="img" aria-label="Showroom wall of furniture handles and fittings"></div>
  <h2 class="about-title">ABOUT VANTO</h2>
  <p class="about-text" style="top:1883px">Pellentesque faucibus Ut accumsan ultricies elit Maecenas at justo id velit placerat molestie Donec</p>
  <p class="about-text" style="top:1945px">dictum lectus non odio Cras a ante vitae enim iaculis aliquam Mauris nunc quam venenatis nec euismod sit amet egestas placerat est Pellentesque habita</p>
  <div class="about-btn">READ MORE</div>
</section>

<section>
  <h2 class="section-title" style="left:126px;top:2282px;font-weight:400">NEWS &amp; BLOGS</h2>

  <article class="card news-card" style="left:126px">
    <div class="card-photo" role="img" aria-label="Open wooden kitchen drawers" style="background:linear-gradient(135deg,#6b6660 0%,#c79a63 50%,#9d6d3d 100%)"></div>
    <h4>Pellentesque faucibus Ut accumsan ultricies Maecenas</h4>
    <p>Duis quam Nam eget lacus Aliquam erat volutpat Quisque dignissim congue leo Mauris vel lacus vitae felis vestibulum</p>
  </article>
  <div class="btn news-btn" style="left:150px">READ MORE</div>

  <article class="card news-card" style="left:448px">
    <div class="card-photo" role="img" aria-label="Living room with sofa, plants and wooden coffee table" style="background:linear-gradient(160deg,#3c5a35 0%,#8a7c6d 45%,#b3aca4 100%)"></div>
    <h4>Mauris vel lacus vitae felis ves-tibulum volutpat Etiam est nunc</h4>
    <p>Duis quam Nam eget lacus Aliquam erat volutpat Quisque dignissim congue leo Mauris vel lacus vitae felis vestibulum</p>
  </article>
  <div class="btn news-btn" style="left:472px">READ MORE</div>

  <article class="card news-card" style="left:772px">
    <div class="card-photo" role="img" aria-label="Bright bathroom with freestanding tub and wooden vanity" style="background:linear-gradient(160deg,#e4e4e2 0%,#c8c6c2 55%,#7a5a3e 100%)"></div>
    <h4>Fusce ultricies orci ac feugiat suscipit leo massa sodales</h4>
    <p>Duis quam Nam eget lacus Aliquam erat volutpat Quisque dignissim congue leo Mauris vel lacus vitae felis vestibulum</p>
  </article>
  <div class="btn news-btn" style="left:796px">READ MORE</div>
</section>

<footer>
  <div class="footer"></div>
  <div class="brand foot-brand" style="left:141px;top:2934px"><span class="brand-dot"></span><span class="brand-name">VANTO</span></div>

  <div class="foot-head" style="left:380px">CONTACT US</div>
  <div class="contact-row" style="top:2974px">
    <svg width="16" height="20" viewBox="0 0 16 20"><path d="M8 1a6 6 0 0 0-6 6c0 5 6 12 6 12s6-7 6-12a6 6 0 0 0-6-6z" fill="none" stroke="#333" stroke-width="1.8"/><circle cx="8" cy="7" r="2" fill="#333"/></svg>
    <span>48 LINDEN ROW #4B<br>HARLOW 20517 HW</span></div>
  <div class="contact-row" style="top:3030px">
    <svg width="16" height="16" viewBox="0 0 16 16"><path d="M3 1l3 3-2 2c1 2 3 4 5 5l2-2 3 3-2 3C7 15 1 9 1 3z" fill="none" stroke="#333" stroke-width="1.6"/></svg>
    <span>555.014.2870</span></div>
  <div class="contact-row" style="top:3067px">
    <svg width="17" height="13" viewBox="0 0 17 13"><rect x="1" y="1" width="15" height="11" fill="none" stroke="#333" stroke-width="1.6"/><path d="M1 1l7.5 6L16 1" fill="none" stroke="#333" stroke-width="1.6"/></svg>
    <span>INFO@VANTO.AT</span></div>

  <div class="foot-head" style="left:676px">COMPANY</div>
  <ul class="foot-list" style="left:678px;top:2958px">
    <li>ABOUT</li><li>BRAND NEW</li><li>CATALOG CONFIGURATOR</li><li>LIGHT CONFIGURATOR</li><li>LAMP</li><li>CONTACT</li>
  </ul>

  <div class="foot-head" style="left:911px">GET IN TOUCH</div>
  <div class="social" style="top:2968px"><i></i>CHIRPLINE</div>
  <div class="social" style="top:3004px"><i></i>FACESPACE</div>
  <div class="social" style="top:3040px"><i></i>WORKLINK</div>
  <div class="social" style="top:3076px"><i></i>SNAPGRAM</div>

  <div class="foot-rule"></div>
  <p class="copy">Copyright © 2019 All right reserved</p>
</footer>

</body>
</html>
```